Communication Coach needs a business card

https://imgvault-example.net/gallery/1839201/40417/40417_22719043_1839201_8c3e7b2f_preview.png

I like this a lot

I want it to include the following

Delia Strennick
M.A.CCC-SLP
555-204-7718
delia.strennick@mailvento.net
Communication Trainer and Executive Function Coaching
Be Confident-Be Authentic- Be Memorable

on back of card
Public Speaking
Executive Function Coaching
Interview Skills
Corporate Workshops
Self Regulation/Confidence Building

Target Market(s)

adults, parents

Contact Information for Business Card

See above description. i included picture of what i like

Requirements
Must have
• two sides, multi colors ,double sided
Nice to have
• I could have a tag line on front such as Be confident-Be memorable -Be authentic
Should not have
• not too busy or creative as needs to work for corporate setting

```html
<!DOCTYPE html>
<html lang="en">
<head>
<meta charset="utf-8">
<title>Delia Strennick – Business Card</title>
<link rel="stylesheet" href="https://fonts.googleapis.com/css2?family=Yellowtail&family=Montserrat:wght@300;400&family=Open+Sans:wght@600&family=Lora:wght@400&display=swap">
<style>
  :root {
    --bg: #2b2b2b;
    --ink: #1d1d1d;
    --paper: #ffffff;
    --black: #0f0f0f;
    --purple: #8c55a2;
    --yellow: #f4d740;
    --pink: #ea5a73;
    --teal: #2fb2a5;
    --green: #97c553;
    --orange: #f07f5b;
  }
  * { box-sizing: border-box; margin: 0; padding: 0; }
  html, body { width: 1200px; height: 900px; overflow: hidden; }
  body {
    background: var(--bg);
    display: flex;
    flex-direction: column;
    align-items: center;
    justify-content: center;
    gap: 44px;
  }
  .card {
    width: 665px;
    height: 380px;
    border-radius: 26px;
    overflow: hidden;
    position: relative;
  }

  /* Back side */
  .card-back { display: flex; flex-direction: column; background: var(--black); }
  .back-tagline {
    height: 78px;
    display: flex; align-items: center; justify-content: center;
    color: var(--paper);
    font-family: "Lora", serif;
    font-size: 30px;
    letter-spacing: 1px;
  }
  .service-stripes { flex: 1; display: flex; }
  .service {
    flex: 1;
    display: flex; align-items: center; justify-content: center;
  }
  .service-label {
    writing-mode: vertical-rl;
    font-family: "Open Sans", sans-serif;
    font-weight: 600;
    font-size: 17px;
    line-height: 1.15;
    text-transform: uppercase;
    color: var(--ink);
    text-align: center;
    white-space: nowrap;
  }
  .purple { background: var(--purple); }
  .yellow { background: var(--yellow); }
  .pink { background: var(--pink); }
  .teal { background: var(--teal); }
  .green { background: var(--green); }
  .orange { background: var(--orange); }

  /* Front side */
  .card-front { background: var(--paper); display: flex; flex-direction: column; }
  .edge-strip { display: flex; }
  .edge-strip span { flex: 1; }
  .edge-top { height: 16px; }
  .edge-bottom { height: 40px; }
  .front-body {
    flex: 1;
    display: flex; flex-direction: column; align-items: center; justify-content: center;
    color: var(--ink);
    padding-left: 40px;
  }
  .name {
    font-family: "Yellowtail", cursive;
    font-size: 80px;
    line-height: 1;
    color: var(--ink);
  }
  .credentials {
    font-family: "Montserrat", sans-serif;
    font-weight: 400;
    font-size: 22px;
    letter-spacing: 1px;
    margin-top: 6px;
  }
  .contact {
    font-family: "Montserrat", sans-serif;
    font-weight: 400;
    font-size: 20px;
    margin-top: 22px;
    display: flex; align-items: center; gap: 12px;
  }
  .contact .divider { width: 1.5px; height: 26px; background: var(--ink); }
  .role {
    font-family: "Lora", serif;
    font-size: 17px;
    letter-spacing: 0.5px;
    text-transform: uppercase;
    margin-top: 14px;
    padding: 5px 8px;
    border-top: 1px solid var(--ink);
    border-bottom: 1px solid var(--ink);
  }
  .front-tagline {
    font-family: "Lora", serif;
    font-size: 18px;
    margin-top: 12px;
  }
</style>
</head>
<body>

  <section class="card card-back" aria-label="Back of card">
    <div class="back-tagline">Be Confident-Be Authentic- Be Memorable</div>
    <div class="service-stripes">
      <div class="service purple"><span class="service-label">Public Speaking</span></div>
      <div class="service yellow"><span class="service-label">Executive Function<br>Coaching</span></div>
      <div class="service pink"><span class="service-label">Interview Skills</span></div>
      <div class="service teal"><span class="service-label">Corporate Workshops</span></div>
      <div class="service green"><span class="service-label">Self Regulation/<br>Confidence Building</span></div>
      <div class="service orange"></div>
    </div>
  </section>

  <section class="card card-front" aria-label="Front of card">
    <div class="edge-strip edge-top">
      <span class="purple"></span><span class="yellow"></span><span class="pink"></span>
      <span class="teal"></span><span class="green"></span><span class="orange"></span>
    </div>
    <div class="front-body">
      <h1 class="name">Delia Strennick</h1>
      <p class="credentials">M.A.CCC-SLP</p>
      <p class="contact">
        <span class="phone">555-204-7718</span>
        <span class="divider"></span>
        <span class="email">delia.strennick@mailvento.net</span>
      </p>
      <p class="role">Communication Trainer and Executive Function Coach</p>
      <p class="front-tagline">Be Confident-Be Authentic- Be Memorable</p>
    </div>
    <div class="edge-strip edge-bottom">
      <span class="purple"></span><span class="yellow"></span><span class="pink"></span>
      <span class="teal"></span><span class="green"></span><span class="orange"></span>
    </div>
  </section>

</body>
</html>
```